Label for Dog Nourishing CBD Balm

Dear Designers,

We are looking for a packaging expert to design our new Hydrating Balm for dogs which contain a relaxing hemp extract (CBD). The product is intended to be massaged on the dog’s paws to make them softer and promote the animal’s well-being :)

Our company is already selling various relaxing cat & dog products, and we would like this new design to reflect the same "style & feeling" as our current products (see attached ZIP file).

Technical aspects:
- The packaging is a 40ml aluminium jar (58mm x 23mm).
- We are looking to design 2 separate labels (one for the front, one for the back)
- The label dimensions should be : 50mm x 50mm
- Please follow technical guidelines from printer (see ZIP file).

Design aspects:
- The design should be compatible with our brand identity (i.e. fluffly, pure, relaxing, positive, clean & natural).
- People should understand what the product "is" and what the product "does" simply from looking at the design.
- The actual balm is white/yellow in color.
- Soft/rounded shapes are preferred.
- Please use our brand's colors (see typo & colors in ZIP file)
- Please use our brand's fonts (see typo & colors in ZIP file)
- Please use our company logo (see ZIP file).
- The design also needs to convey a strong sense of professionalism as we are an animal "healthcare" brand.
- If you want to include a dog picture, we would prefer you to use a picture of our official brand ambassador (see ZIP file).
- Only original work (no plagiarism will be accepted).

Please don't hesitate to send us a message if you have any questions about the brand, the product or the design requirements.

We look forward to seeing your designs & working on this together !

Thanks & regards,
Marcus

Target Market(s)

Dog owners

Font styles to use
Other font styles liked:
• See ZIP file

Requirements
Must have
• Brand fonts (see typo & colors in ZIP file)
Brand colors (see typo & colors in ZIP file)

```html
<!DOCTYPE html>
<html lang="en">
<head>
<meta charset="utf-8">
<title>Lumabalm Soothing Balm Label</title>
<link rel="stylesheet" href="https://fonts.googleapis.com/css2?family=Montserrat:wght@400;600&family=Open+Sans:wght@300;400&family=Roboto+Slab:wght@400&display=swap">
<style>
  :root {
    --backdrop: #525252;
    --label-white: #ffffff;
    --brand-green: #2f9b78;
    --soft-green: #5fb39a;
    --ink-dark: #262b22;
    --ink-body: #2b2b2b;
    --photo-light: #f3f1ee;
    --photo-mid: #d6d2cf;
  }
  html, body {
    margin: 0;
    padding: 0;
    width: 702px;
    height: 1200px;
    overflow: hidden;
    background: var(--backdrop);
  }
  .label-canvas {
    display: block;
    width: 702px;
    height: 1200px;
  }
  .label-disc { fill: var(--label-white); }
  .label-ring { fill: none; stroke: var(--brand-green); stroke-width: 4; }
  .product-arc {
    font-family: "Open Sans", sans-serif;
    font-weight: 300;
    font-size: 50px;
    letter-spacing: 17px;
    fill: var(--soft-green);
  }
  .product-tm {
    font-family: "Open Sans", sans-serif;
    font-weight: 300;
    font-size: 14px;
    fill: var(--soft-green);
  }
  .brand-dot { fill: none; stroke: var(--soft-green); stroke-width: 3; }
  .brand-name {
    font-family: "Montserrat", sans-serif;
    font-weight: 600;
    font-size: 34px;
    letter-spacing: 1px;
    fill: var(--ink-dark);
  }
  .brand-tagline {
    font-family: "Roboto Slab", serif;
    font-size: 14px;
    letter-spacing: 0.5px;
    fill: var(--brand-green);
  }
  .product-title {
    font-family: "Montserrat", sans-serif;
    font-weight: 600;
    font-size: 38px;
    fill: var(--brand-green);
  }
  .divider { stroke: var(--brand-green); stroke-width: 2; }
  .benefits {
    font-family: "Montserrat", sans-serif;
    font-weight: 400;
    font-size: 18px;
    fill: var(--ink-body);
  }
  .dosage {
    font-family: "Montserrat", sans-serif;
    font-size: 10px;
    fill: var(--ink-body);
  }
  .dosage-strong {
    font-weight: 600;
    font-size: 18px;
    fill: var(--brand-green);
  }
  .dosage-sep { fill: var(--brand-green); }
</style>
</head>
<body>
<svg class="label-canvas" viewBox="0 0 702 1200" xmlns="http://www.w3.org/2000/svg">
  <defs>
    <path id="product-name-arc" d="M 139 600 A 212 212 0 0 1 563 600"/>
    <clipPath id="ring-clip"><circle cx="351" cy="600" r="287"/></clipPath>
    <linearGradient id="photo-tone" x1="0" y1="0" x2="0" y2="1">
      <stop offset="0" stop-color="var(--photo-light)"/>
      <stop offset="0.55" stop-color="var(--photo-mid)"/>
      <stop offset="1" stop-color="var(--photo-light)"/>
    </linearGradient>
  </defs>

  <circle class="label-disc" cx="351" cy="600" r="320"/>

  <text class="product-arc">
    <textPath href="#product-name-arc" startOffset="50%" text-anchor="middle">Lumabalm</textPath>
  </text>
  <text class="product-tm" x="520" y="462" transform="rotate(55 520 462)">TM</text>

  <circle class="brand-dot" cx="351" cy="465" r="18"/>
  <text class="brand-name" x="351" y="514" text-anchor="middle">VERDALIS</text>
  <text class="brand-tagline" x="400" y="540" text-anchor="middle">For Animals</text>

  <text class="product-title" x="351" y="597" text-anchor="middle">SOOTHING BALM</text>
  <line class="divider" x1="178" y1="620" x2="524" y2="620"/>
  <text class="benefits" x="351" y="646" text-anchor="middle">REPAIR&#160;&#160;&#160;|&#160;&#160;&#160;NOURISH&#160;&#160;&#160;|&#160;&#160;&#160;PROTECT</text>
  <line class="divider" x1="178" y1="659" x2="524" y2="659"/>

  <text class="dosage" x="351" y="692" text-anchor="middle">CBD 250mg <tspan class="dosage-sep">|</tspan> <tspan class="dosage-strong">40mg</tspan> <tspan class="dosage-sep">|</tspan> 0% THC</text>

  <g clip-path="url(#ring-clip)">
    <rect role="img" aria-label="Photo of the brand's white wrinkled ambassador dog" x="282" y="710" width="158" height="190" rx="30" fill="url(#photo-tone)"/>
  </g>

  <circle class="label-ring" cx="351" cy="600" r="289"/>
</svg>
</body>
</html>
```